High Quality fast food restaurant - Quonfel

Quonfel is a fast food company with its target's focused on logistic, simplicity, high quality, freshness and modern.

We need a web design where the customers can get a complete idea of our high quality completeness, we want to take fast food to a new upper level.

We would like to see the colours of wood and metal. Pictures have been attached of our local.

We would like to have something in similar to: http://www.zq-vorn.com/
Updates

Images for the food we are going to sell can be found here: http://trq.lk/uRTWQ

It will be the images with rice, french fries or pita bread.

Target Market(s)

The fast food eating people between sloppy food and restaurant level.

Industry/Entity Type

Fast Food Restaurant

Requirements
Should not have
• No Flash or Java

```html
<!DOCTYPE html>
<html lang="en">
<head>
<meta charset="utf-8">
<title>Quonfel — High Quality Fast Food</title>
<link rel="stylesheet" href="https://fonts.googleapis.com/css2?family=Arvo:wght@400;700&family=Arimo:wght@400;700&display=swap">
<style>
:root{
  --wood-dark:#2a1410;
  --wood-mid:#3a1d16;
  --orange:#e0561c;
  --orange-dark:#b8400f;
  --page-bg:#ebebeb;
  --panel:#f8f8f8;
  --rule:#c9c9c9;
  --brown-text:#4a2316;
  --red-title:#c2401d;
  --teal:#1fa5bd;
  --grey-text:#9a9a9a;
  --foot-text:#4a4a4a;
  --contact-text:#cf8a6f;
  --green-a:#9bd31a;
  --green-b:#6aa812;
  --green-title:#4b7a12;
  --rib-a:#e18a6c;
  --rib-b:#c24a22;
  --badge-tone:#e2e2e2;
}
*{margin:0;padding:0;box-sizing:border-box}
html,body{width:1200px;height:835px;overflow:hidden}
body{position:relative;background:var(--page-bg);font-family:"Arimo",Arial,sans-serif;color:var(--foot-text)}
.abs{position:absolute}

/* header */
.site-header{left:0;top:0;width:1200px;height:131px;background:linear-gradient(90deg,var(--wood-dark),var(--wood-mid) 40%,var(--wood-dark) 70%,var(--wood-mid));border-top:4px solid var(--orange)}
.brand{left:90px;top:40px;font-family:"Arvo",serif;font-weight:700;font-size:44px;color:#fff;letter-spacing:1px}
.nav-tab{left:527px;top:0;width:90px;height:115px}
.main-nav a{position:absolute;top:56px;font-family:"Arvo",serif;font-size:16.5px;color:#fff;text-decoration:none;transform:translateX(-50%);white-space:nowrap}

/* utility bar */
.search{left:89px;top:142px;width:221px;height:28px;background:#f6f6f6;border:1px solid #d3d3d3;font-size:11px;color:#999;padding:9px 0 0 12px}
.search svg{position:absolute;right:10px;top:6px}
.share-btn{top:148px;height:17px;font-size:10px;font-weight:700;color:#333;background:#eef1f6;border:1px solid #c9ccd4;border-radius:2px;padding:2px 5px 0 5px}
.share-count{top:148px;height:17px;font-size:10px;color:#333;background:#fff;border:1px solid #ccc;border-radius:2px;padding:2px 3px 0}
.call-icon{left:922px;top:121px}
.call-label{left:994px;top:138px;font-size:12.5px;font-weight:700;color:#777}
.call-number{left:974px;top:156px;font-family:"Arvo",serif;font-weight:700;font-size:21px;color:var(--brown-text);letter-spacing:.5px}
.top-rule{left:89px;top:196px;width:1022px;height:1px;background:var(--rule)}

/* hero */
.main-panel{left:89px;top:197px;width:1022px;height:520px;background:linear-gradient(180deg,#f5f5f5,#fafafa)}
.food-combo{left:92px;top:342px;width:280px;height:180px;border-radius:45% 40% 30% 30%;background:radial-gradient(ellipse at 60% 45%,#e2a53c,#b5611c 55%,rgba(230,200,160,0) 72%)}
.food-plate{left:297px;top:376px;width:388px;height:240px;border-radius:50%;background:radial-gradient(ellipse at 50% 40%,#d88a4e,#c2653a 40%,#e8e2dc 62%,rgba(240,240,240,0) 72%)}
.ribbon{font-family:"Arvo",serif}
.ribbon-green{left:90px;top:243px;width:285px;height:100px}
.ribbon-orange{left:573px;top:292px;width:315px;height:100px}
.ribbon h2{position:absolute;font-size:20px;font-weight:700}
.ribbon p{position:absolute;font-family:"Arimo",Arial,sans-serif;font-size:10px;line-height:14px}
.ribbon-green h2{left:26px;top:16px;color:var(--green-title)}
.ribbon-green p{left:28px;top:46px;width:230px;color:#2f3d10}
.ribbon-orange h2{right:24px;top:10px;color:#fff}
.ribbon-orange p{right:24px;top:40px;width:260px;text-align:right;color:#fff}
.offer-badge{left:712px;top:426px;width:152px;height:152px;border-radius:50%;background:var(--badge-tone)}
.slider-arrows{left:101px;top:574px}

/* sidebar */
.sidebar{left:906px;top:197px;width:205px;height:460px;background:#fbfbfb}
.card{left:922px;width:172px;height:208px;background:#fff;border:1px solid #dadada}
.card-media{position:absolute;left:6px;top:6px;width:159px;height:103px}
.card h3{position:absolute;left:10px;top:118px;font-family:"Arvo",serif;font-weight:400;font-size:14px;color:var(--red-title)}
.card p{position:absolute;left:10px;top:141px;width:156px;font-size:11px;line-height:16px;color:var(--grey-text)}
.card a{position:absolute;left:11px;top:180px;font-family:"Arvo",serif;font-size:11.5px;color:var(--teal);text-decoration:none}
.media-promo{background:linear-gradient(135deg,#c9462c,#8a3a1c 50%,#e0b070)}
.media-venue{background:linear-gradient(180deg,#2c2a28,#4a4036 60%,#1c1a18)}

/* contact + footer */
.contact-line{left:0;width:1010px;top:677px;text-align:center;font-size:12.5px;color:var(--contact-text);word-spacing:1px}
.foot-rule{left:118px;top:717px;width:980px;height:1px;background:#d3d3d3}
.foot-nav{left:88px;top:750px;font-size:12.5px;color:var(--foot-text)}
.foot-nav span{margin:0 8px;color:#777}
.copyright{left:88px;top:783px;font-size:12.5px;color:var(--foot-text)}
.social{top:764px;width:24px;height:24px;border-radius:3px}
</style>
</head>
<body>

<header class="site-header abs">
  <svg class="nav-tab abs" viewBox="0 0 90 115" aria-hidden="true"><polygon points="0,0 90,0 90,115 45,96 0,115" fill="var(--orange)"/></svg>
  <div class="brand abs">QUONFEL</div>
  <nav class="main-nav">
    <a href="#" style="left:572px">Home</a>
    <a href="#" style="left:664px">About</a>
    <a href="#" style="left:766px">Products</a>
    <a href="#" style="left:869px">Offers</a>
    <a href="#" style="left:971px">Delivers</a>
    <a href="#" style="left:1079px">Contact</a>
  </nav>
</header>

<div class="search abs">Search
  <svg width="16" height="16" viewBox="0 0 16 16"><circle cx="6" cy="6" r="4.5" fill="none" stroke="#333" stroke-width="2.2"/><line x1="9.5" y1="9.5" x2="14.5" y2="14.5" stroke="#333" stroke-width="3" stroke-linecap="round"/></svg>
</div>

<div class="share-btn abs" style="left:525px">Like</div>
<div class="share-count abs" style="left:570px">3k</div>
<div class="share-btn abs" style="left:598px">Share</div>
<div class="share-count abs" style="left:654px">316</div>

<svg class="call-icon abs" width="60" height="60" viewBox="0 0 60 60" aria-hidden="true">
  <circle cx="29" cy="29" r="28" fill="#fff"/>
  <circle cx="29" cy="29" r="25" fill="var(--teal)"/>
  <path d="M21 17c3-2 5-1 6 2l1 5c0 2-2 3-3 4 1 4 3 7 6 9 1-1 3-3 5-2l4 3c2 2 1 4-1 6-3 3-8 2-13-4-5-6-8-15-5-23z" fill="#fff"/>
</svg>
<div class="call-label abs">Call us or Order</div>
<div class="call-number abs">555 208 4417</div>
<div class="top-rule abs"></div>

<main>
  <div class="main-panel abs"></div>

  <div class="food-combo abs" role="img" aria-label="Photo of a burger with a carton of french fries"></div>
  <div class="food-plate abs" role="img" aria-label="Photo of hot dogs with mustard and ketchup on a white plate"></div>

  <div class="ribbon ribbon-green abs">
    <svg width="285" height="100" viewBox="0 0 285 100" style="position:absolute;left:0;top:0" aria-hidden="true">
      <defs><linearGradient id="gGreen" x1="0" x2="1"><stop offset="0" stop-color="var(--green-b)"/><stop offset="1" stop-color="var(--green-a)"/></linearGradient></defs>
      <polygon points="0,0 280,16 262,70 230,72 228,100 205,74 14,86" fill="url(#gGreen)"/>
      <polygon points="228,100 205,74 262,70" fill="#4f8a10"/>
    </svg>
    <h2>Product Name</h2>
    <p>Praesent et mi purus. Quisque id dolor ut nulla porttitor lobortis at eget lectus.</p>
  </div>

  <div class="ribbon ribbon-orange abs">
    <svg width="315" height="100" viewBox="0 0 315 100" style="position:absolute;left:0;top:0" aria-hidden="true">
      <defs><linearGradient id="gOrange" x1="0" x2="1"><stop offset="0" stop-color="var(--rib-a)"/><stop offset="1" stop-color="var(--rib-b)"/></linearGradient></defs>
      <polygon points="0,12 304,0 314,78 50,68 50,84 2,70" fill="url(#gOrange)"/>
      <polygon points="2,70 50,68 50,84" fill="#9c3a18"/>
    </svg>
    <h2>Product Name</h2>
    <p>Praesent et mi purus. Quisque id dolor ut nulla porttitor lobortis at eget lectus.</p>
  </div>

  <div class="offer-badge abs" role="img" aria-label="Special offer stamp graphic"></div>

  <svg class="slider-arrows abs" width="56" height="26" viewBox="0 0 56 26" aria-label="Slider controls">
    <circle cx="13" cy="13" r="12" fill="#fff" stroke="#ddd"/>
    <circle cx="42" cy="13" r="12" fill="#fff" stroke="#ddd"/>
    <path d="M18 13H8M12 9l-4 4 4 4" fill="none" stroke="var(--orange)" stroke-width="1.6"/>
    <path d="M37 13h10M43 9l4 4-4 4" fill="none" stroke="var(--orange)" stroke-width="1.6"/>
  </svg>

  <aside>
    <div class="sidebar abs"></div>
    <section class="card abs" style="top:217px">
      <div class="card-media media-promo" role="img" aria-label="Photo of grilled salmon with sesame and fresh salad"></div>
      <h3>Offers and Promotions</h3>
      <p>Quisque id dolor ut nulla port titor lobortis at eget lectus.</p>
      <a href="#">View all &nbsp;››</a>
    </section>
    <section class="card abs" style="top:439px">
      <div class="card-media media-venue" role="img" aria-label="Video still of the restaurant interior">
        <svg width="159" height="103" viewBox="0 0 159 103" aria-hidden="true"><circle cx="79" cy="50" r="14" fill="#bbb" opacity=".85"/><polygon points="74,42 74,58 88,50" fill="#555"/></svg>
      </div>
      <h3>About Quonfel</h3>
      <p>Quisque id dolor ut nulla port titor lobortis at eget lectus.</p>
      <a href="#">View more &nbsp;››</a>
    </section>
  </aside>

  <div class="contact-line abs">Location :&nbsp; 18 Larchmont Row, Easthaven, QF204 &nbsp; | &nbsp; Call us : 555 730 1962 &nbsp; | &nbsp; E-mail : info@quonfel.com</div>
</main>

<footer>
  <div class="foot-rule abs"></div>
  <div class="foot-nav abs">Home<span>|</span>About<span>|</span>Products<span>|</span>Offers<span>|</span>Delivers<span>|</span>Contact</div>
  <div class="copyright abs">Copyright &nbsp;©&nbsp; 2013 &nbsp;www.quonfel.com &nbsp;&nbsp;All rights reserved.</div>
  <div class="social abs" style="left:1056px;background:#3b5c9c"></div>
  <div class="social abs" style="left:1087px;background:#3cb8e0"></div>
</footer>

</body>
</html>
```